Football field themed poster-game

I'm looking for a 22" x 29" size poster with a minimum of 300dpi, max of 300mb. File format can be jpg, gif, tiff or bmp. Would like the field portion of the poster to appear like a real grass football field. The field will need makers for each yard. I've added an addition simple clip art that shows another way for yard lines as well.The rest of the layout I would like similar, but made to look more professional. Wording should be the same as in the given draft and located in the same area or close to that area on the poster. The style is open, but should be a little minimalist in nature. Design work has to be original and cannot be taken from trademarked or copyrighted items.
Updates

Project Deadline Extended
Reason: I have 2 or 3 designs that really standout, but I would like to see just a few more.

Target Market(s)

Football fans

Font styles to use
Sans Serif

Colors

Designer to choose colors to be used in the design.

Requirements
Must have
• The design must have the same similar layout as the file I have submitted with the contest. The football field needs to be made to look like a real field with turf. boarders would be nice and a modern look.
Should not have
• hard to read fonts, changes to the major overall layout of poster.

```html
<!DOCTYPE html>
<html lang="en">
<head>
<meta charset="utf-8">
<title>Kickoff Cup Football Game Poster</title>
<link rel="stylesheet" href="https://fonts.googleapis.com/css2?family=Archivo+Black&family=Roboto:wght@400&display=swap">
<style>
  :root {
    --page: #ffffff;
    --ink: #111111;
    --panel: #9e5f48;
    --token: #c98a3d;
    --label-bg: #ffffff;
    --banner: #e0c000;
    --turf-light: #58a332;
    --turf-dark: #3f8a22;
    --chalk: #ffffff;
  }
  html, body {
    margin: 0;
    padding: 0;
    width: 910px;
    height: 1200px;
    overflow: hidden;
    background: var(--page);
  }
  .poster {
    position: relative;
    width: 910px;
    height: 1200px;
  }
  .poster svg {
    display: block;
  }
  .label-text {
    font-family: 'Archivo Black', sans-serif;
    fill: var(--ink);
  }
  .event-name {
    font-family: 'Archivo Black', sans-serif;
    fill: var(--ink);
  }
  .yard-number {
    font-family: 'Roboto', sans-serif;
    fill: var(--chalk);
    font-size: 40px;
    letter-spacing: 9px;
  }
</style>
</head>
<body>
<div class="poster">
<svg width="910" height="1200" viewBox="0 0 910 1200" xmlns="http://www.w3.org/2000/svg">
  <defs>
    <linearGradient id="turf" x1="0" y1="0" x2="1" y2="1">
      <stop offset="0" stop-color="var(--turf-light)"/>
      <stop offset="0.5" stop-color="var(--turf-dark)"/>
      <stop offset="1" stop-color="var(--turf-light)"/>
    </linearGradient>
    <pattern id="mow-stripes" patternUnits="userSpaceOnUse" x="0" y="110" width="910" height="98.1">
      <rect width="910" height="49.05" fill="#000" opacity="0.06"/>
    </pattern>
    <pattern id="yard-lines" patternUnits="userSpaceOnUse" x="0" y="109" width="910" height="49.05">
      <rect x="342" y="0" width="553" height="2" fill="var(--chalk)"/>
    </pattern>
    <pattern id="hash-marks" patternUnits="userSpaceOnUse" x="0" y="109.5" width="910" height="9.81">
      <rect x="348" y="0" width="16" height="2" fill="var(--chalk)"/>
      <rect x="871" y="0" width="16" height="2" fill="var(--chalk)"/>
    </pattern>
  </defs>

  <rect class="page-frame" x="4" y="4" width="902" height="1192" fill="none" stroke="var(--ink)" stroke-width="1.5"/>

  <g class="score-panel">
    <rect x="13" y="11" width="314" height="1174" fill="var(--panel)" stroke="var(--ink)" stroke-width="1.5"/>

    <g class="score-token home-token">
      <circle cx="165" cy="157" r="122" fill="var(--token)" stroke="var(--ink)" stroke-width="1.5"/>
      <rect x="80" y="78" width="170" height="157" fill="var(--label-bg)" stroke="var(--ink)" stroke-width="1.5"/>
    </g>
    <g class="score-label home-score-label">
      <rect x="77" y="295" width="185" height="50" fill="var(--label-bg)" stroke="var(--ink)" stroke-width="1.5"/>
      <text class="label-text" x="169.5" y="320" font-size="36" text-anchor="middle" dominant-baseline="central" transform="rotate(180 169.5 320)">SCORE</text>
    </g>

    <g class="game-title">
      <rect x="40" y="418" width="257" height="360" fill="var(--banner)" stroke="var(--ink)" stroke-width="1.5"/>
      <text class="event-name" x="0" y="0" font-size="50" text-anchor="middle" dominant-baseline="central" transform="translate(200 598) rotate(90)">KICKOFF</text>
      <text class="event-name" x="0" y="0" font-size="50" text-anchor="middle" dominant-baseline="central" transform="translate(136 598) rotate(90)">CUP</text>
    </g>

    <g class="score-label visitor-score-label">
      <rect x="77" y="845" width="185" height="49" fill="var(--label-bg)" stroke="var(--ink)" stroke-width="1.5"/>
      <text class="label-text" x="169.5" y="870" font-size="36" text-anchor="middle" dominant-baseline="central">SCORE</text>
    </g>
    <g class="score-token visitor-token">
      <circle cx="165" cy="1037" r="122" fill="var(--token)" stroke="var(--ink)" stroke-width="1.5"/>
      <rect x="80" y="960" width="170" height="157" fill="var(--label-bg)" stroke="var(--ink)" stroke-width="1.5"/>
    </g>
  </g>

  <g class="field">
    <rect x="342" y="11" width="553" height="1171" fill="url(#turf)"/>
    <rect x="342" y="110" width="553" height="981" fill="url(#mow-stripes)"/>
    <rect x="342" y="11" width="553" height="1171" fill="none" stroke="var(--chalk)" stroke-width="2"/>

    <rect class="yard-lines" x="342" y="109" width="553" height="984" fill="url(#yard-lines)"/>
    <rect class="hash-marks" x="342" y="110" width="553" height="981" fill="url(#hash-marks)"/>

    <rect x="612" y="130" width="12" height="2" fill="var(--chalk)"/>
    <rect x="612" y="1070" width="12" height="2" fill="var(--chalk)"/>
    <rect x="563" y="11" width="2" height="8" fill="var(--chalk)"/>
    <rect x="671" y="11" width="2" height="8" fill="var(--chalk)"/>
    <rect x="563" y="1174" width="2" height="8" fill="var(--chalk)"/>
    <rect x="671" y="1174" width="2" height="8" fill="var(--chalk)"/>

    <g class="end-zone-label home-label">
      <rect x="473" y="35" width="296" height="63" fill="var(--label-bg)"/>
      <text class="label-text" x="621" y="66.5" font-size="40" text-anchor="middle" dominant-baseline="central" transform="rotate(180 621 66.5)">HOME</text>
    </g>
    <g class="end-zone-label visitor-label">
      <rect x="473" y="1095" width="296" height="64" fill="var(--label-bg)"/>
      <text class="label-text" x="621" y="1127" font-size="40" text-anchor="middle" dominant-baseline="central">VISITORS</text>
    </g>

    <g class="yard-numbers left-side" text-anchor="middle" dominant-baseline="central">
      <text class="yard-number" transform="translate(427 208) rotate(90)">10</text>
      <text class="yard-number" transform="translate(427 306) rotate(90)">20</text>
      <text class="yard-number" transform="translate(427 404) rotate(90)">30</text>
      <text class="yard-number" transform="translate(427 502) rotate(90)">40</text>
      <text class="yard-number" transform="translate(427 600) rotate(90)">50</text>
      <text class="yard-number" transform="translate(427 698) rotate(90)">40</text>
      <text class="yard-number" transform="translate(427 797) rotate(90)">30</text>
      <text class="yard-number" transform="translate(427 895) rotate(90)">20</text>
      <text class="yard-number" transform="translate(427 993) rotate(90)">10</text>
    </g>
    <g class="yard-numbers right-side" text-anchor="middle" dominant-baseline="central">
      <text class="yard-number" transform="translate(812 208) rotate(-90)">10</text>
      <text class="yard-number" transform="translate(812 306) rotate(-90)">20</text>
      <text class="yard-number" transform="translate(812 404) rotate(-90)">30</text>
      <text class="yard-number" transform="translate(812 502) rotate(-90)">40</text>
      <text class="yard-number" transform="translate(812 600) rotate(-90)">50</text>
      <text class="yard-number" transform="translate(812 698) rotate(-90)">40</text>
      <text class="yard-number" transform="translate(812 797) rotate(-90)">30</text>
      <text class="yard-number" transform="translate(812 895) rotate(-90)">20</text>
      <text class="yard-number" transform="translate(812 993) rotate(-90)">10</text>
    </g>
  </g>
</svg>
</div>
</body>
</html>
```